Business Card Design for a Design/Build Firm

Kestrel Forge Partners, Inc. is a firm providing construction professional project management and architectural design services to an international clientele. Contemporary. "Green" movement aware. Business card to have back design/logo. Cards will be on high gloss paper

Target Market(s)

Building Developers and Owners

Industry/Entity Type

Construction

Requirements
Nice to have
• We really would like to use the acronym "KFP" as main focal point fo card design. Company will be known as KFP.
Should not have
• No globes or abstract images of buildings.

```html
<!DOCTYPE html>
<html lang="en">
<head>
<meta charset="utf-8">
<title>Kestrel Forge Partners – Business Card</title>
<link rel="stylesheet" href="https://fonts.googleapis.com/css2?family=Mulish:wght@400;500;700&display=swap">
<style>
  :root {
    --brand-green: #21ad48;
    --card-white: #ffffff;
    --backdrop: #2b2b2b;
    --card-shadow: rgba(0, 0, 0, 0.35);
  }
  html, body {
    margin: 0;
    padding: 0;
    width: 1200px;
    height: 900px;
    overflow: hidden;
    background: var(--backdrop);
  }
  .stage {
    position: relative;
    width: 1200px;
    height: 900px;
  }
  .card {
    position: absolute;
    top: 308px;
    width: 513px;
    height: 284px;
    box-shadow: 0 4px 14px var(--card-shadow);
  }
  .card--back { left: 72px; }
  .card--front { left: 615px; }
  .card svg { display: block; }
  .type { font-family: "Mulish", "Avenir Next", sans-serif; }
  .monogram { font-weight: 400; }
  .tagline { font-weight: 700; font-size: 12.5px; }
  .person-name { font-weight: 500; font-size: 17px; }
  .person-role { font-weight: 400; font-size: 13px; }
  .contact-line { font-weight: 400; font-size: 13px; }
  .fill-green { fill: var(--brand-green); }
  .fill-white { fill: var(--card-white); }
</style>
</head>
<body>
<main class="stage">

  <!-- Card back: oversized monogram on green -->
  <section class="card card--back" aria-label="Business card back">
    <svg width="513" height="284" viewBox="0 0 513 284">
      <defs>
        <clipPath id="back-clip"><rect width="513" height="284"/></clipPath>
      </defs>
      <g clip-path="url(#back-clip)">
        <rect class="fill-green" width="513" height="284"/>
        <g class="type monogram fill-white" font-size="340">
          <text x="6" y="266" textLength="170" lengthAdjust="spacingAndGlyphs">K</text>
          <text x="196" y="266" textLength="150" lengthAdjust="spacingAndGlyphs">F</text>
          <text x="360" y="266" textLength="150" lengthAdjust="spacingAndGlyphs">P</text>
        </g>
        <g class="type tagline fill-white">
          <text x="260" y="224">Kestrel Forge</text>
          <text x="260" y="240">Partners, Inc.</text>
        </g>
      </g>
    </svg>
  </section>

  <!-- Card front: monogram, swoosh band, contact details -->
  <section class="card card--front" aria-label="Business card front">
    <svg width="513" height="284" viewBox="0 0 513 284">
      <defs>
        <clipPath id="front-clip"><rect width="513" height="284"/></clipPath>
      </defs>
      <g clip-path="url(#front-clip)">
        <rect class="fill-white" width="513" height="284"/>

        <g class="type monogram fill-green" font-size="155">
          <text x="40" y="140" textLength="240" lengthAdjust="spacingAndGlyphs">KFP</text>
        </g>
        <g class="type tagline fill-green">
          <text x="300" y="41">Kestrel Forge</text>
          <text x="300" y="58">Partners, Inc.</text>
        </g>

        <path class="swoosh-band fill-green"
              d="M0,168 C120,212 330,186 513,92 L513,284 L0,284 Z"/>
        <path class="swoosh-line" fill="none" stroke="var(--card-white)" stroke-width="3"
              d="M0,175 C120,218 330,194 513,103"/>

        <g class="type fill-white">
          <text class="person-name" x="57" y="236">Mara Ellison</text>
          <text class="person-role" x="57" y="256">managing director</text>
        </g>

        <g class="contact-icons fill-white">
          <rect x="292" y="218" width="11" height="8" rx="1"/>
          <path d="M292.5,218.5 L297.5,223 L302.5,218.5" fill="none" stroke="var(--brand-green)" stroke-width="1.2"/>
          <rect x="294" y="251" width="7" height="11" rx="1.5"/>
          <rect x="295.5" y="253" width="4" height="5" fill="var(--brand-green)"/>
        </g>
        <g class="type contact-line fill-white">
          <text x="312" y="226">47 Alder Lane</text>
          <text x="312" y="244">Brookfield, New York 10482</text>
          <text x="312" y="262">555 214 67 30</text>
        </g>
      </g>
    </svg>
  </section>

</main>
</body>
</html>
```